Print Ad for Pilates Studio

I need a full color 1/4 page ad (size 5" tall x 3 3/4" wide) that includes our logo at top with this text:
Intro Specials for New Students:
3 Private Sessions for only $150 (normally $75/session)
3 Group Reformer Classes for $49 (normally $35/class)
5 Bootcamp Classes for only $29 (normally $15/class0
and might include the tree graphic, and the three small logos (QRN, Green-certified and Top Pick) at bottom plus our phone number really big
555-214-3096 and e-mail MarissaTolvane@mailbrook.example and website www.steadycorefit.example
Should look enticing and CLEAN

Target Market(s)

Older affluent market

Industry/Entity Type

Group

Requirements
Must have
• Clean lines
• Bold
• Classy
• some space
• Makes you want to take action now
Nice to have
• photo of people doing pilates
• Bold color like yellow, green, burgundy

```html
<!DOCTYPE html>
<html lang="en">
<head>
<meta charset="utf-8">
<title>Steady Core Fit – Intro Specials</title>
<link rel="stylesheet" href="https://fonts.googleapis.com/css2?family=Open+Sans:wght@400;600;700;800&display=swap">
<style>
  :root {
    --page-bg: #e9e9e6;
    --paper: #ffffff;
    --leaf-green: #a9d05c;
    --leaf-light: #c4e08a;
    --forest: #2d4621;
    --olive-text: #3e4a2b;
    --amber: #c98a2c;
    --link-blue: #1f4f9c;
  }
  * { margin: 0; padding: 0; box-sizing: border-box; }
  html, body { width: 968px; height: 1200px; overflow: hidden; background: var(--page-bg); }
  body { position: relative; font-family: "Open Sans", Arial, sans-serif; }

  .flyer {
    position: absolute; left: 85px; top: 31px;
    width: 664px; height: 948px;
    background: var(--paper);
    transform: scale(1.2); transform-origin: top left;
    overflow: hidden;
  }
  .green-field {
    position: absolute; left: 52px; top: 62px; width: 566px; height: 832px;
    background: radial-gradient(ellipse at 60% 40%, var(--leaf-light), var(--leaf-green) 70%);
    box-shadow: 0 0 22px 14px var(--leaf-green);
    border-radius: 6px;
  }
  .tree-art {
    position: absolute; left: 440px; top: 110px; width: 190px; height: 420px;
    background: radial-gradient(ellipse at 55% 35%, rgba(230,244,200,.75), rgba(200,228,150,0) 70%);
  }
  .brand { position: absolute; left: 125px; top: 118px; display: flex; align-items: center; gap: 12px; }
  .brand-dot { width: 58px; height: 58px; border-radius: 50%; background: var(--amber); }
  .brand-name { font-weight: 700; font-size: 34px; color: var(--forest); line-height: 1; }
  .brand-tag {
    position: absolute; left: 245px; top: 168px; width: 222px; height: 18px;
    background: var(--forest); color: #fff; font-size: 12px; font-weight: 600;
    text-align: center; line-height: 18px; border: 1px solid #fff;
  }
  .headline {
    position: absolute; left: 95px; top: 222px;
    font-size: 30px; font-weight: 800; line-height: 42px; color: var(--amber);
  }
  .swoosh { position: absolute; left: 95px; top: 306px; }
  .offers { position: absolute; left: 97px; top: 338px; width: 470px; color: var(--olive-text); }
  .offer { margin-bottom: 8px; }
  .offer-title { font-size: 22px; font-weight: 700; display: flex; align-items: center; gap: 8px; line-height: 34px; }
  .price-tag {
    background: var(--forest); color: #fff; font-size: 22px; font-weight: 700;
    padding: 0 8px; border-radius: 3px; line-height: 34px;
  }
  .offer-note { font-size: 15px; line-height: 19px; }
  .phone {
    position: absolute; left: 0; width: 664px; top: 596px; text-align: center;
    font-size: 56px; font-weight: 800; color: var(--amber);
    -webkit-text-stroke: 2px #fff; paint-order: stroke fill;
  }
  .email {
    position: absolute; left: 0; width: 664px; top: 668px; text-align: center;
    font-size: 20px; color: var(--forest);
  }
  .dancers-art {
    position: absolute; left: 110px; top: 712px; width: 450px; height: 112px;
    background: linear-gradient(180deg, rgba(30,40,20,.15), rgba(30,40,20,.55));
    border-radius: 40px 40px 4px 4px;
  }
  .badges { position: absolute; left: 235px; top: 834px; display: flex; gap: 14px; }
  .badge { width: 58px; height: 56px; background: #fff; border: 2px solid #9aa; border-radius: 4px; }
  .badge.star { background: #2c5aa0; border-color: #1d3f73; width: 52px; }
  .badge.round { border-radius: 8px; border-color: #2f8a6a; width: 62px; }
  .website {
    position: absolute; left: 0; width: 664px; top: 900px; text-align: center;
    font-size: 19px; color: var(--link-blue);
  }
</style>
</head>
<body>
  <main class="flyer">
    <div class="green-field"></div>
    <div class="tree-art" role="img" aria-label="Faint illustrated leafy tree decoration"></div>

    <header>
      <div class="brand"><span class="brand-dot"></span><span class="brand-name">Steady Core Fit</span></div>
      <div class="brand-tag">Pilates &amp; Spiral Motion Studio</div>
    </header>

    <h1 class="headline">INTRO SPECIALS FOR<br>NEW STUDENTS:</h1>
    <svg class="swoosh" width="150" height="26" viewBox="0 0 150 26">
      <path d="M0 20 Q60 -2 150 10 Q70 6 0 24 Z" fill="#2d4621"/>
      <path d="M0 24 Q70 8 150 12" stroke="#fff" stroke-width="2" fill="none"/>
    </svg>

    <section class="offers">
      <div class="offer">
        <div class="offer-title">3 Private Sessions for only <span class="price-tag">$150</span></div>
        <div class="offer-note">(normally $75/session)</div>
      </div>
      <div class="offer">
        <div class="offer-title">3 Group Reformer Classes for <span class="price-tag">$49</span></div>
        <div class="offer-note">(normally $35/class)</div>
      </div>
      <div class="offer">
        <div class="offer-title">5 Bootcamp Classes for only <span class="price-tag">$29</span></div>
        <div class="offer-note">(normally $15/class0 and might include the tree graphic, and the three small logos (QRN, Green-certified and Top Pick) at bottom plus our phone number really big</div>
      </div>
    </section>

    <div class="phone">555-214-3096</div>
    <div class="email">e-mail MarissaTolvane@mailbrook.example</div>

    <div class="dancers-art" role="img" aria-label="Silhouettes of dancers in flowing movement sequence"></div>

    <div class="badges">
      <div class="badge"></div>
      <div class="badge star"></div>
      <div class="badge round"></div>
    </div>

    <div class="website">www.steadycorefit.example</div>
  </main>
</body>
</html>
```